Media Browser and player web application

I need to redesign a web application that enables to browse a media server (Lumarra) contents (images, audio, video) and play it in a web player.

Current implementation of the application can be seen at: http://www.kelbofaq.net/content/demonstration-lumarra-pro-online-media-browser

This refresh is aiming to:
1) make the application simpler, based on typology (think Panelix Tile style, VidHalo, Flickro); a simple fan concept is here: http://tow.gandeliq.net/lumarra/
2) make the application work on desktop as well as touch screen devices (ie no hover functionality, no pagination, large touch controls)
3) fast (remove unnecessary animations)
4) design with the app being responsive in mind

The attached UX designs show the basic flows in the application. Please note that the placement of controls (for example) is not set in stone and I welcome your input on the layout.

Ideally the default theme will be dark. Items' thumbnails will be square place holders, with images fit in them depending on the item icons' aspect ratio.

Also attaching the product's logo (Lumarra) and icon. The web application's name is ClipRoamer (or Lumarra ClipRoamer), so it should be included in the design (the UX designs include place holder Lumarra logo in the left top corner).

The main categories for each file type are (you will have to provide an icon for each of these):
- Audio: Albums, Artists, Album artists, Folders, Genres, Composers, Titles, Random music, Random albums, Last listened, Playlists, Online
- Image: Albums, Folders, Year, Month, Playlists, Online
- Video: Titles, Movies, Series, Folders, Last viewed, Last added, Genres, Actors, Directors, Producers, Release years, Playlists, Online
Updates

Target Market(s)

Mostly tech enthusiasts who want to stream their media over the internet to their devices.

Industry/Entity Type

Artists

Requirements
Must have
• Designs for all the provided UX designs
Touch-friendly web application design
High-res (Retina) assets
Light, type based Tile-like design
Nice to have
• Responsive web version
Dark and Light theme switching.
Should not have
• Chrome
Heavy graphics (eg backgrounds) that take time to load

```html
<!DOCTYPE html>
<html lang="en">
<head>
<meta charset="utf-8">
<title>Lumarra ClipRoamer – Audio</title>
<link rel="stylesheet" href="https://fonts.googleapis.com/css2?family=Questrial&display=swap">
<style>
  :root {
    --yellow: #f4e212;
    --yellow-dark: #d9c90e;
    --olive: #7a7000;
    --ink: #000000;
    --grey-text: #8a8a8a;
    --pill: #f3f3f3;
    --btn-grey: #5a5a5a;
    --white: #ffffff;
    --band-light: #efefef;
    --band-tint: #f7f1b8;
  }
  * { box-sizing: border-box; margin: 0; padding: 0; }
  html, body { width: 1200px; height: 715px; overflow: hidden; background: var(--white); }
  body { font-family: "Questrial", "Century Gothic", sans-serif; color: var(--ink); position: relative; }

  .footer-band {
    position: absolute; left: 0; bottom: 0; width: 1200px; height: 190px;
    background: linear-gradient(175deg, var(--white) 0%, var(--band-light) 55%, var(--band-tint) 100%);
  }

  .brand { position: absolute; left: 83px; top: 62px; display: flex; align-items: center; gap: 10px; }
  .brand-mark { width: 44px; height: 44px; background: var(--yellow); border-radius: 6px; }
  .brand-name { font-size: 44px; line-height: 1; color: var(--ink); }

  .account { position: absolute; left: 782px; top: 66px; display: flex; align-items: center; gap: 10px; }
  .avatar { width: 39px; height: 39px; border: 2px solid var(--yellow); background: linear-gradient(#8a8a8a, #3b3b3b); }
  .account-pill { width: 275px; height: 34px; border-radius: 17px; background: var(--pill); display: flex; align-items: center; justify-content: space-between; padding: 0 18px; font-size: 13.5px; }
  .welcome { color: var(--grey-text); }
  .welcome .user { color: var(--olive); }
  .sign-out { color: var(--olive); display: flex; align-items: center; gap: 5px; }

  .breadcrumb { position: absolute; left: 96px; top: 159px; display: flex; align-items: center; gap: 8px; font-size: 13.5px; color: var(--grey-text); }
  .breadcrumb .current { color: var(--olive); }
  .breadcrumb .sep { color: var(--grey-text); }

  .toolbar { position: absolute; left: 1028px; top: 154px; display: flex; gap: 7px; }
  .tool-btn { width: 30px; height: 30px; display: flex; align-items: center; justify-content: center; }
  .tool-btn.menu { background: var(--yellow); }
  .tool-btn.search { background: var(--btn-grey); }

  .tiles { position: absolute; left: 88px; top: 201px; display: grid; grid-template-columns: repeat(6, 145px); grid-auto-rows: 145px; column-gap: 8px; row-gap: 10px; }
  .tile { position: relative; border: 3.5px solid var(--yellow); background: var(--white); display: flex; flex-direction: column; align-items: center; }
  .tile svg.folder { margin-top: 35px; width: 90px; height: 56px; }
  .tile .label { position: absolute; top: 116px; left: 0; right: 0; text-align: center; font-size: 13.5px; }
  .tile.current { background: var(--yellow); border-color: var(--yellow); }
  .tile.current svg.note { margin-top: 36px; width: 62px; height: 66px; }
  .back-btn { position: absolute; left: 0; top: 0; width: 31px; height: 29px; background: var(--yellow-dark); display: flex; align-items: center; justify-content: center; }
</style>
</head>
<body>

<div class="footer-band" role="img" aria-label="Decorative background ribbons in grey and yellow"></div>

<header>
  <div class="brand">
    <span class="brand-mark"></span>
    <span class="brand-name">Lumarra</span>
  </div>
  <div class="account">
    <div class="avatar" role="img" aria-label="User profile photo"></div>
    <div class="account-pill">
      <span class="welcome">Welcome, <span class="user">Dale Morrow</span></span>
      <span class="sign-out">
        <svg width="15" height="13" viewBox="0 0 15 13"><circle cx="6.5" cy="6.5" r="5" fill="none" stroke="#000" stroke-width="2.2"/><path d="M6 6.5 H14 M11 3.5 L14 6.5 L11 9.5" fill="none" stroke="#000" stroke-width="2"/></svg>
        Sign Out
      </span>
    </div>
  </div>
</header>

<nav class="breadcrumb">
  <svg width="22" height="22" viewBox="0 0 22 22"><path d="M11 2 L21 11 H18 V20 H13 V14 H9 V20 H4 V11 H1 Z" fill="#000"/></svg>
  <span>» AUDIO</span>
  <span><span class="sep">»</span> <span class="current">My Personal Collection</span></span>
</nav>

<div class="toolbar">
  <div class="tool-btn menu"><svg width="20" height="16" viewBox="0 0 20 16"><rect y="1" width="20" height="2.6" fill="#fff"/><rect y="6.7" width="20" height="2.6" fill="#fff"/><rect y="12.4" width="20" height="2.6" fill="#fff"/></svg></div>
  <div class="tool-btn search"><svg width="20" height="20" viewBox="0 0 20 20"><circle cx="8" cy="8" r="6" fill="none" stroke="#fff" stroke-width="2"/><path d="M12.5 12.5 L18.5 18.5" stroke="#fff" stroke-width="2.4"/></svg></div>
</div>

<main class="tiles">
  <div class="tile current">
    <span class="back-btn"><svg width="20" height="14" viewBox="0 0 20 14"><path d="M0 7 L8 0 V4 H20 V10 H8 V14 Z" fill="#000"/></svg></span>
    <svg class="note" viewBox="0 0 62 66"><rect x="14" y="4" width="6" height="50" fill="#000"/><rect x="52" y="0" width="6" height="50" fill="#000"/><path d="M14 4 L58 0 V12 L14 16 Z" fill="#000"/><ellipse cx="11" cy="54" rx="11" ry="8.5" fill="#000"/><ellipse cx="49" cy="52" rx="11" ry="8.5" fill="#000"/></svg>
    <span class="label">music</span>
  </div>
  <div class="tile"><svg class="folder" viewBox="0 0 90 56"><path d="M0 4 Q0 0 4 0 H24 L30 5 H80 Q84 5 84 9 V10 H6 L0 50 Z" fill="#000"/><path d="M8 13 H90 L82 56 H0 Z" fill="#000"/></svg><span class="label">Artists</span></div>
  <div class="tile"><svg class="folder" viewBox="0 0 90 56"><path d="M0 4 Q0 0 4 0 H24 L30 5 H80 Q84 5 84 9 V10 H6 L0 50 Z" fill="#000"/><path d="M8 13 H90 L82 56 H0 Z" fill="#000"/></svg><span class="label">Album Artists</span></div>
  <div class="tile"><svg class="folder" viewBox="0 0 90 56"><path d="M0 4 Q0 0 4 0 H24 L30 5 H80 Q84 5 84 9 V10 H6 L0 50 Z" fill="#000"/><path d="M8 13 H90 L82 56 H0 Z" fill="#000"/></svg><span class="label">Folders</span></div>
  <div class="tile"><svg class="folder" viewBox="0 0 90 56"><path d="M0 4 Q0 0 4 0 H24 L30 5 H80 Q84 5 84 9 V10 H6 L0 50 Z" fill="#000"/><path d="M8 13 H90 L82 56 H0 Z" fill="#000"/></svg><span class="label">Genres</span></div>
  <div class="tile"><svg class="folder" viewBox="0 0 90 56"><path d="M0 4 Q0 0 4 0 H24 L30 5 H80 Q84 5 84 9 V10 H6 L0 50 Z" fill="#000"/><path d="M8 13 H90 L82 56 H0 Z" fill="#000"/></svg><span class="label">Composers</span></div>
  <div class="tile"><svg class="folder" viewBox="0 0 90 56"><path d="M0 4 Q0 0 4 0 H24 L30 5 H80 Q84 5 84 9 V10 H6 L0 50 Z" fill="#000"/><path d="M8 13 H90 L82 56 H0 Z" fill="#000"/></svg><span class="label">Titles</span></div>
  <div class="tile"><svg class="folder" viewBox="0 0 90 56"><path d="M0 4 Q0 0 4 0 H24 L30 5 H80 Q84 5 84 9 V10 H6 L0 50 Z" fill="#000"/><path d="M8 13 H90 L82 56 H0 Z" fill="#000"/></svg><span class="label">Random</span></div>
  <div class="tile"><svg class="folder" viewBox="0 0 90 56"><path d="M0 4 Q0 0 4 0 H24 L30 5 H80 Q84 5 84 9 V10 H6 L0 50 Z" fill="#000"/><path d="M8 13 H90 L82 56 H0 Z" fill="#000"/></svg><span class="label">Playlists</span></div>
  <div class="tile"><svg class="folder" viewBox="0 0 90 56"><path d="M0 4 Q0 0 4 0 H24 L30 5 H80 Q84 5 84 9 V10 H6 L0 50 Z" fill="#000"/><path d="M8 13 H90 L82 56 H0 Z" fill="#000"/></svg><span class="label">Online</span></div>
</main>

</body>
</html>
```